Develop a PowerPoint template based on existing logo for a non-profit international alliance of professionals.
Presentations that will be made with this template will include mostly bullet point text and some tables. SOme images could also be included.

Target Market(s)

Governments, private funders

Industry/Entity Type

Non-Profit

Requirements
Must have
• clean and modern feel
Should not have
• no background in the slide area

```html
<!DOCTYPE html>
<html lang="en">
<head>
<meta charset="utf-8">
<title>Northgate Alliance – Presentation Template</title>
<link href="https://fonts.googleapis.com/css2?family=Source+Sans+3:wght@400;600;700&display=swap" rel="stylesheet">
<style>
  :root {
    --red: #d7252b;
    --red-dark: #a8151b;
    --red-light: #ea4b4f;
    --ink: #3a3a3a;
    --ink-soft: #5a5a5a;
    --paper: #ffffff;
    --stage: #ececea;
    --photo-a: #3e5a78;
    --photo-b: #a88a6c;
    --photo-c: #d9cfc2;
    --bar-orange: #f29a1f;
    --bar-yellow: #f4d32a;
    --bar-green: #6cae3c;
    --bar-blue: #3f6fb5;
  }
  * { box-sizing: border-box; margin: 0; padding: 0; }
  html, body { width: 1200px; height: 900px; overflow: hidden; }
  body {
    background: var(--stage);
    font-family: "Source Sans 3", Arial, sans-serif;
    color: var(--ink);
    position: relative;
  }
  .slide {
    position: absolute;
    width: 560px;
    height: 380px;
    background: var(--paper);
    overflow: hidden;
    box-shadow: 0 2px 8px rgba(0,0,0,.18);
  }
  .slide--cover   { left: 24px;  top: 50px; }
  .slide--bullets { left: 616px; top: 50px; }
  .slide--chart   { left: 24px;  top: 470px; }
  .slide--closing { left: 616px; top: 470px; background: var(--red); }

  .brand {
    position: absolute;
    display: flex;
    align-items: center;
    gap: 10px;
    font-weight: 700;
    color: var(--red);
    letter-spacing: .04em;
  }
  .brand__dot { width: 30px; height: 30px; border-radius: 50%; background: var(--red); }
  .slide--cover .brand { left: 34px; top: 36px; font-size: 24px; }
  .slide--closing .brand { left: 0; right: 0; top: 160px; justify-content: center; color: #fff; font-size: 28px; }
  .slide--closing .brand__dot { background: #fff; width: 34px; height: 34px; }

  .decor-dots {
    position: absolute;
    right: 0; top: 0;
    width: 300px; height: 230px;
    background: radial-gradient(circle at 70% 30%, #dcdcdc 0%, #efefef 45%, rgba(255,255,255,0) 75%);
  }
  .cover__title {
    position: absolute; left: 34px; top: 180px;
    font-size: 29px; font-weight: 700; color: var(--ink);
  }
  .cover__subtitle {
    position: absolute; left: 34px; top: 218px;
    font-size: 20px; font-weight: 400; color: var(--ink-soft);
  }
  .cover__band {
    position: absolute; left: 0; right: 0; top: 262px; height: 96px;
    background: var(--red);
  }
  .cover__photo {
    position: absolute; left: 175px; right: 0; top: 262px; height: 96px;
    background: linear-gradient(90deg, var(--photo-a), var(--photo-b) 45%, var(--photo-c) 70%, var(--photo-a));
  }

  .header { position: absolute; left: 0; top: 0; width: 560px; height: 90px; }
  .header__title {
    position: absolute; left: 22px; top: 20px;
    color: #fff; font-size: 21px; font-weight: 700;
  }
  .header__photo {
    position: absolute; left: 260px; right: 0; top: 0; height: 58px;
    background: linear-gradient(90deg, var(--photo-a), var(--photo-c) 35%, var(--photo-b) 65%, var(--photo-a));
  }

  .bullets {
    position: absolute; left: 48px; top: 108px; width: 460px;
    list-style: none; font-size: 13px; line-height: 1.4; color: var(--ink);
  }
  .bullets li { position: relative; padding-left: 16px; margin-bottom: 14px; }
  .bullets li::before {
    content: ""; position: absolute; left: 0; top: 4px;
    width: 9px; height: 9px; border-radius: 50%; background: var(--red);
  }

  .footer-url {
    position: absolute; right: 22px; bottom: 14px;
    font-size: 10px; letter-spacing: .14em; color: var(--ink-soft);
  }

  .chart-text {
    position: absolute; left: 24px; top: 150px; width: 180px;
    font-size: 12px; line-height: 1.35; color: var(--ink);
  }
  .chart-text p + p { margin-top: 10px; }
  .chart-text .lead { font-weight: 700; }
  .chart {
    position: absolute; left: 215px; top: 135px; width: 320px; height: 200px;
  }
  .chart text { font-family: "Source Sans 3", Arial, sans-serif; font-size: 11px; fill: var(--ink); }

  .closing__arc { position: absolute; left: 0; top: 0; width: 560px; height: 110px; }
  .closing__glow {
    position: absolute; left: 120px; top: 230px; width: 320px; height: 150px;
    background: radial-gradient(ellipse at 50% 80%, var(--red-light) 0%, rgba(234,75,79,0) 70%);
  }
  .closing__contact {
    position: absolute; left: 0; right: 0; top: 222px;
    text-align: center; color: #fbdcdc; font-size: 10px; letter-spacing: .04em;
  }
</style>
</head>
<body>

<section class="slide slide--cover">
  <div class="decor-dots" role="img" aria-label="Faint grey dotted decoration"></div>
  <div class="brand"><span class="brand__dot"></span>NORTHGATE ALLIANCE</div>
  <h1 class="cover__title">Our Software Delivery Process</h1>
  <p class="cover__subtitle">Agile Development</p>
  <div class="cover__band"></div>
  <div class="cover__photo" role="img" aria-label="Photo strip of professionals working in a lab and office"></div>
</section>

<section class="slide slide--bullets">
  <svg class="header" viewBox="0 0 560 90" aria-hidden="true">
    <path d="M0 0 H560 V58 Q300 92 0 66 Z" fill="var(--red)"/>
    <path d="M0 72 Q300 98 560 64" fill="none" stroke="var(--red-dark)" stroke-width="3"/>
  </svg>
  <div class="header__photo" role="img" aria-label="Photo strip of researchers at work"></div>
  <h2 class="header__title">YOUR TITLE HERE</h2>
  <ul class="bullets">
    <li>We’re looking for a template that represents our culture - new, exciting, bold, edgy, and technology-driven. From the one design, we need two templates - one with a black background and one with a white background.</li>
    <li>The dark template will be used for corporate communications to investors, franchisees, and customers. The white template will be used for internal training to employees and franchisees.</li>
    <li>A consistent look and feel, color palette, and layout should be used. Both logos are attached.</li>
  </ul>
  <div class="footer-url">www.northgateforum.org</div>
</section>

<section class="slide slide--chart">
  <svg class="header" viewBox="0 0 560 90" aria-hidden="true">
    <path d="M0 0 H560 V58 Q300 92 0 66 Z" fill="var(--red)"/>
    <path d="M0 72 Q300 98 560 64" fill="none" stroke="var(--red-dark)" stroke-width="3"/>
  </svg>
  <div class="header__photo" role="img" aria-label="Photo strip of researchers at work"></div>
  <h2 class="header__title">YOUR TITLE HERE</h2>
  <div class="chart-text">
    <p class="lead">Lorem ipsum dolor sit amet, consectetur adipiscing elit, sed do eiusmod tempor incididunt ut labore et dolore magna aliqua.</p>
    <p>Ut enim ad minim veniam, quis nostrud exercitation ullamco laboris nisi ut aliquip ex ea commodo consequat.</p>
  </div>
  <svg class="chart" viewBox="0 0 320 200" role="img" aria-label="Bar chart of four series across four quarters">
    <g stroke="#d6d6d6" stroke-width="1">
      <line x1="50" y1="20" x2="310" y2="20"/>
      <line x1="50" y1="55" x2="310" y2="55"/>
      <line x1="50" y1="90" x2="310" y2="90"/>
      <line x1="50" y1="125" x2="310" y2="125"/>
      <line x1="50" y1="160" x2="310" y2="160"/>
    </g>
    <g text-anchor="end">
      <text x="44" y="24">11000</text>
      <text x="44" y="59">10000</text>
      <text x="44" y="94">9000</text>
      <text x="44" y="129">8000</text>
      <text x="44" y="164">7000</text>
    </g>
    <g>
      <rect x="62"  y="70"  width="12" height="90" fill="var(--bar-orange)"/>
      <rect x="75"  y="40"  width="12" height="120" fill="var(--bar-yellow)"/>
      <rect x="88"  y="110" width="12" height="50" fill="var(--bar-green)"/>
      <rect x="101" y="125" width="12" height="35" fill="var(--bar-blue)"/>

      <rect x="127" y="30"  width="12" height="130" fill="var(--bar-orange)"/>
      <rect x="140" y="60"  width="12" height="100" fill="var(--bar-yellow)"/>
      <rect x="153" y="100" width="12" height="60" fill="var(--bar-green)"/>
      <rect x="166" y="118" width="12" height="42" fill="var(--bar-blue)"/>

      <rect x="192" y="50"  width="12" height="110" fill="var(--bar-orange)"/>
      <rect x="205" y="25"  width="12" height="135" fill="var(--bar-yellow)"/>
      <rect x="218" y="95"  width="12" height="65" fill="var(--bar-green)"/>
      <rect x="231" y="112" width="12" height="48" fill="var(--bar-blue)"/>

      <rect x="257" y="35"  width="12" height="125" fill="var(--bar-orange)"/>
      <rect x="270" y="55"  width="12" height="105" fill="var(--bar-yellow)"/>
      <rect x="283" y="90"  width="12" height="70" fill="var(--bar-green)"/>
      <rect x="296" y="105" width="12" height="55" fill="var(--bar-blue)"/>
    </g>
    <line x1="50" y1="160" x2="310" y2="160" stroke="#9a9a9a" stroke-width="1"/>
    <g text-anchor="middle">
      <text x="88"  y="178">Q1</text>
      <text x="153" y="178">Q2</text>
      <text x="218" y="178">Q3</text>
      <text x="283" y="178">Q4</text>
    </g>
  </svg>
  <div class="footer-url">www.northgateforum.org</div>
</section>

<section class="slide slide--closing">
  <svg class="closing__arc" viewBox="0 0 560 110" aria-hidden="true">
    <path d="M0 0 H560 V40 Q300 90 0 60 Z" fill="var(--red-light)"/>
    <path d="M0 66 Q300 100 560 46" fill="none" stroke="var(--red-dark)" stroke-width="3"/>
  </svg>
  <div class="brand"><span class="brand__dot"></span>NORTHGATE ALLIANCE</div>
  <p class="closing__contact">800-555-0142 ext. 200 | Email | info@northgateforum.org | www.northgateforum.org</p>
  <div class="closing__glow" role="img" aria-label="Soft lighter red dotted decoration"></div>
</section>

</body>
</html>
```